NYC and MIAMI Trendy Womans Boutique Custom Mailing Packaging

Im looking for help designing custom mailing pouches for my woman's retail store. Weve been doing a lot of online sales lately and Its time to upgrade to custom packaging. I want it to look fun and playful but not too childish or cheesy.
Please see our website www.tavorila.com and our instagram account @tavorila to get a feel for our brand.

Target Market(s)

From teens- 60 year old

Industry/Entity Type

Clothing Brand

Colors
feeeee
fff9f9
fdf3f8

Requirements
Must have
• Pink :) I need it to be girly, fun, but also classy and sophisticated
Should not have
• Look childish or cheesy

```html
<!DOCTYPE html>
<html lang="en">
<head>
<meta charset="UTF-8">
<title>Tavorila Mailer Pouch</title>
<link href="https://fonts.googleapis.com/css2?family=Playfair+Display:wght@700&family=Dancing+Script:wght@600&display=swap" rel="stylesheet">
<style>
  :root {
    --backdrop: #8a8588;
    --pouch-light: #edc7d8;
    --pouch-stripe: #e6bcd0;
    --pouch-edge: #e2b3c9;
    --seal-pink: #e0a3bf;
    --logo-white: #f1eeee;
    --script-ink: #111111;
  }
  * { margin: 0; padding: 0; box-sizing: border-box; }
  html, body {
    width: 1200px;
    height: 900px;
    overflow: hidden;
    background: var(--backdrop);
  }
  .canvas {
    position: relative;
    width: 1200px;
    height: 900px;
  }
  .mailer-pouch {
    position: absolute;
    left: 336px;
    top: 124px;
    width: 529px;
    height: 652px;
    background:
      repeating-linear-gradient(90deg,
        var(--pouch-light) 0 42px,
        var(--pouch-stripe) 42px 84px);
    box-shadow: inset 0 0 40px var(--pouch-edge);
  }
  .brand-seal {
    position: absolute;
    left: 457px;
    top: 317px;
    width: 286px;
    height: 286px;
    border-radius: 50%;
    background: var(--seal-pink);
    box-shadow: 0 2px 6px rgba(120, 60, 90, 0.25);
    display: flex;
    align-items: center;
    justify-content: center;
  }
  .brand-name {
    font-family: "Playfair Display", serif;
    font-weight: 700;
    font-size: 40px;
    letter-spacing: 2px;
    color: var(--logo-white);
  }
  .thank-you-line {
    position: absolute;
    left: 336px;
    width: 529px;
    top: 660px;
    text-align: center;
    font-family: "Dancing Script", cursive;
    font-weight: 600;
    font-size: 30px;
    color: var(--script-ink);
  }
</style>
</head>
<body>
  <main class="canvas">
    <section class="mailer-pouch" aria-label="Striped pink mailing pouch"></section>
    <div class="brand-seal">
      <span class="brand-name">TAVORILA</span>
    </div>
    <p class="thank-you-line">Thank you for shopping with us!</p>
  </main>
</body>
</html>
```